Stylish High End Wedding Videography/Films Website (BDMR)

We need a modern and high-end website look for our wedding video and films business. We films weddings all over the United Kingdom and at European destinations so need something to reflect our work. The website should be visually stunning with images and videos being the focal point as this is what our services are;

I have uploads of some items I like and the features the site needs to have. These have been taken from other websites using standout features.

We need the following pages;

1 - Homepage
2 - Films Index Page
3 - Individual Films Page
4 - Prices / Collection Page
5 - Reviews
6 - Options
7 - About
8 - Contact
9 - Blog Index
10 - Blog Page

All pages must be consistent so have a similar style.

Pages on menu:
Films
Prices
Reviews
Options
About
Contact

We require a responsive look too. Over 90% of our visitors access the website via their mobile devices.

Please use the colours from our logo to incorporate into the website.

Target Market(s)

Wedding Couples

Industry/Entity Type

Wedding Photography

Number of Pages Required

5+ page

Font styles to use
Sans Serif
Script

Requirements
Must have
• The logo must be in the centre of the menu at the top.

Social icons at the bottom of the page.

Use only two fonts including Lore which is supplied
Nice to have
• Different video for each page on the top header. This will play behind the menu.

```html
<!DOCTYPE html>
<html lang="en">
<head>
<meta charset="utf-8">
<title>BDMR – Ben Dormer Wedding Films</title>
<link rel="stylesheet" href="https://fonts.googleapis.com/css2?family=Jost:wght@400;500&family=Lato:ital,wght@0,400;0,700;1,400&display=swap">
<style>
:root{
  --gold:#a88a4e;
  --gold-soft:#c9ad74;
  --ink:#1b1b1b;
  --body:#6a6a6a;
  --white:#ffffff;
  --footer:#3b3b3b;
  --footer-text:#e4e4e4;
  --rule:#8a8a8a;
}
*{box-sizing:border-box;margin:0;padding:0}
html,body{width:1200px;height:4570px;overflow:hidden}
body{position:relative;background:var(--white);font-family:"Lato",sans-serif;color:var(--body)}
.abs{position:absolute}
.head-font{font-family:"Jost",sans-serif}

/* hero */
.hero{left:0;top:0;width:1200px;height:628px;
  background:linear-gradient(90deg,#7fb1c8 0%,#9cc3d3 35%,#b7cfd6 55%,#d9c6b4 75%,#c9a995 100%)}
.hero-photo{left:560px;top:0;width:640px;height:628px;
  background:radial-gradient(ellipse at 55% 45%,rgba(236,205,185,.85),rgba(210,190,175,.4) 55%,rgba(0,0,0,0) 75%)}
.nav a{position:absolute;top:56px;font-family:"Jost",sans-serif;font-size:14px;letter-spacing:.5px;color:var(--white);text-decoration:none;text-transform:uppercase}
.nav a.active{color:var(--gold)}
.brand{left:450px;top:30px;width:300px;text-align:center;color:var(--white)}
.brand-dot{width:26px;height:26px;border:2px solid var(--white);border-radius:50%;margin:0 auto 12px}
.brand-name{font-family:"Jost",sans-serif;font-size:19px;letter-spacing:5px}
.brand-sub{font-family:"Jost",sans-serif;font-size:9px;letter-spacing:4px;margin-top:2px}
.hero-title{left:112px;top:250px;font-family:"Jost",sans-serif;font-weight:500;font-size:62px;color:var(--white);letter-spacing:1px}
.hero-text{left:112px;top:340px;width:500px;font-size:14px;line-height:25px;color:var(--white)}
.btn-gold{left:112px;top:410px;width:153px;height:50px;background:var(--gold);color:var(--white);font-family:"Jost",sans-serif;font-size:13px;font-weight:500;display:flex;align-items:center;justify-content:center;gap:8px}
.play{left:893px;top:300px}

/* sections */
.section-mark{width:22px;height:22px;border:2px solid var(--gold);border-radius:50%}
.section-title{font-family:"Jost",sans-serif;font-weight:500;font-size:34px;color:var(--ink);letter-spacing:.5px;text-transform:uppercase}
.centered{left:0;width:1200px;text-align:center}

.about-photo{left:112px;top:719px;width:452px;height:490px;background:linear-gradient(100deg,#f1f1f1 0%,#cfcfcf 40%,#5a5452 70%,#2a2626 100%)}
.about-text{left:632px;top:888px;width:455px;font-size:13.5px;line-height:24px}
.about-text p+p{margin-top:24px}
.btn-outline{left:632px;top:1102px;width:153px;height:50px;border:2px solid var(--gold);color:var(--gold);font-family:"Jost",sans-serif;font-size:13px;font-weight:500;display:flex;align-items:center;justify-content:center;gap:8px}

.diary{left:0;top:1438px;width:1200px;height:772px;display:grid;grid-template-columns:repeat(3,1fr);grid-template-rows:repeat(3,1fr);gap:2px}
.tile{width:100%;height:100%}

.film{display:flex;align-items:center;justify-content:center}
.view-all{top:3157px;font-family:"Jost",sans-serif;font-size:13px;color:var(--gold);text-decoration:underline}

.reviews{left:0;top:3255px;width:1200px;height:428px;background:linear-gradient(90deg,#5a4f55 0%,#8a8fa8 30%,#b9b4c4 55%,#c8b4b0 75%,#6a5a58 100%)}
.review-text{left:270px;top:3440px;width:660px;text-align:center;font-style:italic;font-size:13px;line-height:29px;color:var(--white)}
.review-name{top:3537px;font-size:13px;font-weight:700;color:var(--white)}
.review-name span{font-weight:400;color:#f0e0c0}
.stars{top:3570px;color:#f4a51c;font-size:17px;letter-spacing:2px}

.insta{left:112px;top:3891px;width:976px;height:264px;display:grid;grid-template-columns:repeat(4,1fr)}

/* footer */
.footer{left:0;top:4237px;width:1200px;height:333px;background:var(--footer)}
.badge{left:144px;top:4275px;width:112px;height:112px;border-radius:50%;background:#f4e8a8;border:3px solid #e5d27a}
.social{top:4412px;width:36px;height:36px;border:1.5px solid var(--white);border-radius:50%}
.f-head{top:4281px;font-family:"Jost",sans-serif;font-size:13px;color:var(--white);text-decoration:underline;text-transform:uppercase}
.f-list{list-style:none;font-size:12.5px;color:var(--footer-text)}
.f-list li{height:34.5px}
.f-list li::before{content:"»";margin-right:14px;color:var(--white)}
.contact-row{left:868px;display:flex;gap:18px;font-size:12.5px;line-height:20px;color:var(--footer-text)}
.icon-circle{width:32px;height:32px;border-radius:50%;background:var(--white);display:flex;align-items:center;justify-content:center;flex:none}
.f-rule{left:112px;top:4510px;width:976px;height:1px;background:var(--rule)}
.copyright{top:4532px;font-size:13px;color:var(--white)}
</style>
</head>
<body>

<!-- hero -->
<div class="abs hero" role="img" aria-label="Video still: bride and groom embracing by the sea"></div>
<div class="abs hero-photo"></div>
<nav class="nav">
  <a class="active" style="left:124px">Home</a>
  <a style="left:199px">Films</a>
  <a style="left:272px">Prices</a>
  <a style="left:351px">Reviews</a>
  <a style="left:829px">Options</a>
  <a style="left:923px">About</a>
  <a style="left:1006px">Contact</a>
</nav>
<div class="abs brand">
  <div class="brand-dot"></div>
  <div class="brand-name">BEN DORMER</div>
  <div class="brand-sub">WEDDING FILMS</div>
</div>
<h1 class="abs hero-title">BEN DORMER</h1>
<p class="abs hero-text">Ben Dormer is a wedding filmmaker based in the North East of England. We film weddings in a fun and natural way.</p>
<div class="abs btn-gold">GET STARTED
  <svg width="13" height="13" viewBox="0 0 14 14"><circle cx="7" cy="7" r="7" fill="#fff"/><path d="M5.5 4l3 3-3 3" stroke="#a88a4e" stroke-width="1.8" fill="none"/></svg>
</div>
<svg class="abs play" width="60" height="60" viewBox="0 0 60 60"><circle cx="30" cy="30" r="27" fill="rgba(255,255,255,.25)" stroke="#fff" stroke-width="3"/><circle cx="30" cy="30" r="20" fill="#fff"/><path d="M25 20l14 10-14 10z" fill="#333"/></svg>

<!-- about -->
<div class="abs about-photo" role="img" aria-label="Portrait of the filmmaker"></div>
<div class="abs section-mark" style="left:636px;top:776px"></div>
<h2 class="abs section-title" style="left:632px;top:805px;font-size:32px">About Ben Dormer</h2>
<div class="abs about-text">
  <p>I'm a filmmaker who loves documenting couples' most important day of their lives. Based in County Durham I film weddings mostly in the North East of England however regularly travel around the UK and Europe.</p>
  <p>I first picked up a video camera when I was 8 years old making home movies documenting family holidays and events and it led me onto gaining a degree in TV and Radio Production at University. After University I set up the very first Community.</p>
</div>
<div class="abs btn-outline">VIEW MORE
  <svg width="13" height="13" viewBox="0 0 14 14"><circle cx="7" cy="7" r="7" fill="#a88a4e"/><path d="M5.5 4l3 3-3 3" stroke="#fff" stroke-width="1.8" fill="none"/></svg>
</div>

<!-- wedding diary -->
<div class="abs section-mark" style="left:589px;top:1315px"></div>
<h2 class="abs section-title centered" style="top:1343px">Wedding Diary</h2>
<div class="abs diary">
  <div class="tile" role="img" aria-label="Groom carrying bride on a beach" style="background:linear-gradient(#f3d9b5,#e7c9a3)"></div>
  <div class="tile" role="img" aria-label="Couple with bouquet at golden hour" style="background:linear-gradient(#c9a57a,#5a4c44)"></div>
  <div class="tile" role="img" aria-label="Couple under confetti" style="background:linear-gradient(#8a7466,#3b3432)"></div>
  <div class="tile" role="img" aria-label="Couple kissing with sparklers" style="background:linear-gradient(#5d6b55,#3a3430)"></div>
  <div class="tile" role="img" aria-label="Couple walking down a tree-lined path" style="background:linear-gradient(#3c5a66,#1f2e35)"></div>
  <div class="tile" role="img" aria-label="Couple in a decorated reception hall" style="background:linear-gradient(#e9ddc8,#b8a38a)"></div>
  <div class="tile" role="img" aria-label="First dance at the reception" style="background:linear-gradient(#d6b8c2,#8d6f78)"></div>
  <div class="tile" role="img" aria-label="Guests clapping for the couple outdoors" style="background:linear-gradient(#c8b57a,#6e6a4a)"></div>
  <div class="tile" role="img" aria-label="Couple kissing in a field" style="background:linear-gradient(#ead9c0,#9c7a4f)"></div>
</div>

<!-- films -->
<div class="abs section-mark" style="left:589px;top:2291px"></div>
<h2 class="abs section-title centered" style="top:2326px">Prefer Something A Bit More Funky</h2>
<div class="abs film" role="img" aria-label="Film still: couple touching foreheads by the sea" style="left:112px;top:2416px;width:976px;height:389px;background:linear-gradient(90deg,#e8d7c6,#c9c2bf 50%,#d9cfc8)">
  <svg width="52" height="52" viewBox="0 0 52 52"><circle cx="26" cy="26" r="24" fill="none" stroke="#fff" stroke-width="2.5"/><path d="M21 16l15 10-15 10z" fill="none" stroke="#fff" stroke-width="2.5"/></svg>
</div>
<div class="abs film" role="img" aria-label="Film still: couple at a beach ceremony" style="left:112px;top:2819px;width:482px;height:286px;background:linear-gradient(#dcd6d2,#cdbfae)">
  <svg width="52" height="52" viewBox="0 0 52 52"><circle cx="26" cy="26" r="24" fill="none" stroke="#fff" stroke-width="2.5"/><path d="M21 16l15 10-15 10z" fill="none" stroke="#fff" stroke-width="2.5"/></svg>
</div>
<div class="abs film" role="img" aria-label="Film still: couple walking along the shore" style="left:606px;top:2819px;width:482px;height:286px;background:linear-gradient(#b9c5cd,#c9b8a6)">
  <svg width="52" height="52" viewBox="0 0 52 52"><circle cx="26" cy="26" r="24" fill="none" stroke="#fff" stroke-width="2.5"/><path d="M21 16l15 10-15 10z" fill="none" stroke="#fff" stroke-width="2.5"/></svg>
</div>
<div class="abs view-all centered">VIEW ALL »</div>

<!-- reviews -->
<div class="abs reviews" role="img" aria-label="Blurred photo of a couple under falling confetti"></div>
<div class="abs section-mark" style="left:589px;top:3322px;border-color:#fff"></div>
<h2 class="abs section-title centered" style="top:3359px;color:#fff">What Our Clients Say</h2>
<p class="abs review-text">Lorem ipsum dolor sit amet, consectetur adipiscing elit, sed do eiusmod tempor incididunt ut labore et dolore magna aliqua. Ut enim ad minim veniam, quis nostrud exercitation ullamco laboris nisi ut aliquip ex ea commodo consequat. Duis aute irure dolor in reprehenderit in voluptate velit esse cillum.</p>
<div class="abs review-name centered">JOHN SMITH , <span>Founder</span></div>
<div class="abs stars centered">★★★★★</div>
<svg class="abs" style="left:582px;top:3606px" width="36" height="12" viewBox="0 0 36 12"><circle cx="6" cy="6" r="4.5" fill="#fff"/><circle cx="18" cy="6" r="4.5" fill="none" stroke="#fff" stroke-width="1.5"/><circle cx="30" cy="6" r="4.5" fill="#fff"/></svg>

<!-- instagram -->
<div class="abs section-mark" style="left:589px;top:3754px"></div>
<h2 class="abs section-title centered" style="top:3793px">Follow Us On Instagram</h2>
<div class="abs insta">
  <div class="tile" role="img" aria-label="Couple embracing with a white bouquet" style="background:linear-gradient(#ddd8d4,#7a6f6a)"></div>
  <div class="tile" role="img" aria-label="Bride under confetti" style="background:linear-gradient(#c9b9a4,#e5d7c5)"></div>
  <div class="tile" role="img" aria-label="Couple in warm sunlight" style="background:linear-gradient(#f3d2b0,#c89a8c)"></div>
  <div class="tile" role="img" aria-label="Couple kissing at sunset" style="background:linear-gradient(#e6cfb8,#8a6e62)"></div>
</div>

<!-- footer -->
<footer class="abs footer"></footer>
<div class="abs badge" role="img" aria-label="Featured listing badge"></div>
<div class="abs social" style="left:143px" aria-label="Social link"></div>
<div class="abs social" style="left:190px" aria-label="Social link"></div>
<div class="abs social" style="left:238px" aria-label="Social link"></div>

<div class="abs f-head" style="left:412px">Quick Links</div>
<ul class="abs f-list" style="left:412px;top:4316px">
  <li>Home</li><li>About Us</li><li>Photos</li><li>Reviews</li><li>Contact Us</li>
</ul>
<div class="abs f-head" style="left:634px">Other Links</div>
<ul class="abs f-list" style="left:634px;top:4316px">
  <li>FAQ</li><li>Help Service</li><li>Terms Of Use</li><li>Privacy Policy</li><li>Videos</li>
</ul>
<div class="abs f-head" style="left:868px">Contact Us</div>
<div class="abs contact-row" style="top:4314px">
  <div class="icon-circle"><svg width="14" height="16" viewBox="0 0 14 18"><path d="M7 1a6 6 0 0 0-6 6c0 4.5 6 10 6 10s6-5.5 6-10a6 6 0 0 0-6-6z" fill="none" stroke="#a88a4e" stroke-width="1.8"/><circle cx="7" cy="7" r="2" fill="#a88a4e"/></svg></div>
  <div>639 , Nemo enim ipsam<br>United States</div>
</div>
<div class="abs contact-row" style="top:4380px;align-items:center">
  <div class="icon-circle"><svg width="14" height="14" viewBox="0 0 16 16"><path d="M3 1l3 3-2 2a9 9 0 0 0 6 6l2-2 3 3-2 2C7 15 1 9 1 3z" fill="#a88a4e"/></svg></div>
  <div>07000 123 456</div>
</div>
<div class="abs contact-row" style="top:4436px;align-items:center">
  <div class="icon-circle"><svg width="15" height="12" viewBox="0 0 16 12"><rect x="1" y="1" width="14" height="10" rx="1.5" fill="none" stroke="#a88a4e" stroke-width="1.6"/><path d="M1.5 1.5L8 7l6.5-5.5" fill="none" stroke="#a88a4e" stroke-width="1.6"/></svg></div>
  <div>films@bendormer.example</div>
</div>
<div class="abs f-rule"></div>
<div class="abs copyright centered">© 2020 Ben Dormer. All Rights Reserved</div>

</body>
</html>
```